Cambodia 501c3 flyer design

I need a flyer to build interest and awareness for a school year kick off event in October for our charity school in rural Cambodia. I have text and photos available and just need help getting a professional look and feel. (Other projects may follow, including logo and web redesign.)

Founded in 2004 by Lars Trulsen, The Riverside Learning House at Prek Sala is a 501(c)(3) organization dedicated to breaking the cycle of poverty of some of Cambodia's poorest children by providing a rigorous core K-9 education that emphasizes English proficiency.

"The board of directors of The Riverside Learning House at Prek Sala invites you to our annual visit to Prek Sala, Cambodia to help launch the new school year. The trip is open to everyone-you do not need to be a current donor to attend.

If you have been interested in visiting an educational project that works for hundreds of the poorest children in Cambodia, here is your chance. This school is a lifeline for these children and their families, providing education, transportation, uniforms, and two meals a day."
Updates

Hi everyone! I am really impressed by these designs and there are some really promising directions. One thing I would like to see is revisions with more white space, with the blues and yellows as more accents. Any sort of conservative sans serif font is fine.

Also, in general I will need the final in some kind of editable format where I can make basic text updates. I can do this with either AI or Word. 

The use of the kids' photos is great! I will issue a preliminary cut in the next few days. Thank you all again very much for your work on the behalf of the school and children of Cambodia!

Reason: Hi all, I am going to extend the deadline by 7 days so that I have a chance to review the comps with the other board members. That meeting takes place on 21 April so I should be able to proceed shortly thereafter.

Target Market(s)

For this piece, current donors and prospective donors

Industry/Entity Type

Education

Requirements
Nice to have
• Use any elements from www.riversidelearnhouse.org as you see fit. There are lots of photos of the students that might be helpful. There are also more photos of the school at my Flickr account at
http://www.photoshelfhub.com/photos/58172046@K07/page4/

```html
<!DOCTYPE html>
<html lang="en">
<head>
<meta charset="utf-8">
<title>The Riverside Learning House at Prek Sala – 2013 School Year Kick Off Tour</title>
<link rel="stylesheet" href="https://fonts.googleapis.com/css2?family=Oswald:wght@400;500;600&family=Cabin:wght@400;500&family=Tinos:ital,wght@1,700&display=swap">
<style>
  :root {
    --yellow: #fff27a;
    --yellow-pale: #fffbb0;
    --yellow-bar: #fff06a;
    --maroon: #8e3b3f;
    --slate: #6b6b5a;
    --teal: #1c5570;
    --navy: #17178f;
    --ochre: #8c6a10;
    --beige: #dcd8a8;
    --blue-light: #a9ccf5;
    --blue-mid: #7fb0ee;
    --red: #a50f12;
    --white: #ffffff;
  }
  * { margin: 0; padding: 0; box-sizing: border-box; }
  html, body { width: 927px; height: 1200px; overflow: hidden; background: var(--white); }
  .flyer { position: relative; width: 927px; height: 1200px; overflow: hidden; background: var(--white); font-family: "Cabin", Arial, sans-serif; }
  .abs { position: absolute; }
  .backdrop { position: absolute; left: 0; top: 0; }

  .title {
    left: 0; width: 927px; top: 14px; text-align: center;
    font-family: "Oswald", sans-serif; font-weight: 500; font-variant: small-caps;
    font-size: 52px; line-height: 60px; color: var(--maroon); letter-spacing: 0.5px;
  }
  .tour {
    left: 40px; top: 92px; font-family: "Oswald", sans-serif; font-weight: 500;
    font-size: 22px; line-height: 26px; color: var(--maroon); text-transform: uppercase;
  }
  .tour .label { color: var(--slate); }
  .tour .date { display: block; padding-left: 150px; }
  .tour-rule { left: 482px; top: 97px; width: 445px; height: 20px; background: var(--teal); }

  .photo { border-radius: 2px; }
  .photo-intro { left: 14px; top: 202px; width: 291px; height: 220px; background: linear-gradient(135deg, #6f4a3a, #c39a86 55%, #e7e3ea); }
  .intro { left: 336px; top: 204px; width: 560px; color: var(--teal); font-size: 14.6px; line-height: 19.5px; }
  .intro p + p { margin-top: 19px; }

  .about-box { left: 0; top: 438px; width: 682px; height: 276px; background: var(--yellow-pale); }
  .about-head { left: 0; top: 450px; width: 682px; height: 30px; background: var(--yellow-bar); color: var(--navy); font-weight: 500; font-size: 14px; line-height: 30px; text-align: center; }
  .about { left: 44px; top: 496px; width: 612px; color: var(--navy); font-size: 14.2px; line-height: 19px; text-align: center; }
  .about p + p { margin-top: 18px; }
  .photo-class { left: 690px; top: 438px; width: 237px; height: 138px; background: linear-gradient(160deg, #7a6f63, #d9dce4 60%, #3c3f5c); }
  .photo-kitchen { left: 690px; top: 586px; width: 237px; height: 128px; background: linear-gradient(200deg, #c9c6c0, #6e6a62 60%, #3a3530); }

  .photo-grad { left: 14px; top: 732px; width: 278px; height: 278px; background: linear-gradient(150deg, #3b3631, #a98a7a 50%, #bcc6e0); }
  .details-head { left: 300px; top: 733px; width: 627px; height: 15px; background: var(--beige); color: var(--ochre); font-weight: 500; font-size: 12.5px; line-height: 15px; padding-left: 4px; }
  .details { left: 302px; top: 750px; width: 615px; color: var(--ochre); font-size: 13.4px; line-height: 17.2px; }
  .details p + p { margin-top: 17px; }

  .contact { left: 27px; top: 1076px; width: 420px; color: var(--red); font-family: Arial, Helvetica, sans-serif; font-weight: bold; font-size: 10.3px; line-height: 12.2px; }
  .contact p + p { margin-top: 12px; }
  .board { display: grid; grid-template-columns: 190px 82px auto; margin-top: 12px; }
  .mission-box { left: 452px; top: 1062px; width: 475px; height: 138px; background: var(--blue-mid); }
  .mission { left: 466px; top: 1082px; width: 452px; color: var(--white); font-family: "Tinos", "Times New Roman", serif; font-style: italic; font-weight: 700; font-size: 11.2px; line-height: 14.4px; text-align: left; }
</style>
</head>
<body>
<div class="flyer">

  <svg class="backdrop" width="927" height="1200" viewBox="0 0 927 1200" aria-hidden="true">
    <path d="M0 0 H927 V140 C760 128 560 205 360 196 C220 190 90 150 0 175 Z" fill="var(--yellow)"/>
    <path d="M0 175 C90 150 220 190 360 196 C560 205 760 128 927 140 V160 C760 150 560 228 360 216 C210 208 90 172 0 195 Z" fill="#f2f2f2"/>
    <path d="M0 1000 C240 980 520 1050 927 995 V1012 C520 1070 240 1000 0 1020 Z" fill="#ececec"/>
    <path d="M0 1045 C260 1000 560 1050 927 1010 V1200 H0 Z" fill="var(--blue-light)"/>
    <path d="M0 1045 C260 1000 560 1050 927 1010 V1020 C560 1062 260 1012 0 1057 Z" fill="#f4f8ff" opacity="0.8"/>
  </svg>

  <h1 class="abs title">The Riverside Learning House at Prek Sala</h1>
  <div class="abs tour"><span class="label">Header:</span> The 2013 School Year Kick Off Tour<span class="date">October 1, 2013</span></div>
  <div class="abs tour-rule"></div>

  <div class="abs photo photo-intro" role="img" aria-label="Photo of a smiling schoolgirl in uniform"></div>
  <div class="abs intro">
    <p>The board of directors of The Riverside Learning House at Prek Sala invites you to our annual visit to Prek Sala, Cambodia to help launch the new school year. The trip is open to everyone--you do not need to be a current donor to attend.</p>
    <p>If you have been interested in visiting an educational project that works for hundreds of the poorest children in Cambodia, here is your chance. This school is a lifeline for these children and their families, providing education, transportation, uniforms, and two meals a day.</p>
    <p>Join us for the experience of a lifetime. You will be touched by the spirit of these children and their drive to learn. And, the local town of Siem Reap is the base from which to visit Angkor Wat, the UNESCO World Heritage site that should not be missed.</p>
  </div>

  <div class="abs about-box"></div>
  <h2 class="abs about-head">ABOUT THE SCHOOL</h2>
  <div class="abs about">
    <p>Founded in April 2004 by Lakeport, CA educator Lars Trulsen, the Riverside Learning House at Prek Sala provides a basic education aimed at reaching Cambodia's poorest youth.</p>
    <p>After having been both touched by the genuine kindness of the locals and yet unsettled by the widespread poverty suffered in the aftermath of the Vietnam War and Khmer Rouge era, Lars led efforts to turn an underutilized building into a thriving school in a region where education in neither compulsory nor affordable for the poorest families.</p>
    <p>In 2012, the school also reached the maximum enrollment of 345 students in twelve classes in grades K-9. The curriculum emphasizes English and all general subjects such as Khmer (the local language), math, science, and social studies.</p>
  </div>
  <div class="abs photo photo-class" role="img" aria-label="Photo of students in uniform gathered with a visitor"></div>
  <div class="abs photo photo-kitchen" role="img" aria-label="Photo of cooks preparing a meal in large woks"></div>

  <div class="abs photo photo-grad" role="img" aria-label="Photo of a boy holding his school certificate"></div>
  <h2 class="abs details-head">THE DETAILS</h2>
  <div class="abs details">
    <p>Monday, September 30. You should plan on arriving in Siem Reap either from Bangkok or Phnom Penh. There will be a cocktail party and mixer for visitors, donors and guests that evening. The location and time will be announced on the website.</p>
    <p>Tuesday, October 1.&nbsp; We will meet in the lobby of the ___________Hotel at 8:30 a.m. to board private, air conditioned buses to the campus. The trip takes about 90 minutes. We will open as the students sing the Cambodian national anthem, and the students will put on a brief performance of local dances. All guests will have special "VIP" seating and will listen to brief talks by Lars Trulsen, the founder, as well as the local provincial governor. The school will provide lunch, and there will be plenty of time for a tour of the campus as well as, most importantly, to interact with the boys and girls, many of whom are very eager to practice their English. We will return to town around 3:00 p.m. and will meet for dinner on Siem Reap's famous "Pub Street".</p>
    <p>The cost: You are responsible for your own travel arrangements, but there is no cost to attend the event. Lunch and transportation to and from the school is provided by our donors.</p>
  </div>

  <div class="abs contact">
    <p>For more details, visit www.riversidelearnhouse.org/2013trip for travel tips and other suggestions about what to see and do in Cambodia.</p>
    <p>If you have questions about this once in a lifetime opportunity, please contact one of the board members below. We are happy to help with specific travel tips and recommendations.</p>
    <div class="board">
      <span>Lars Trulsen, founder and president</span><span>000-000-0000</span><span>email@email.com</span>
      <span>Peter Vance, secretary and director</span><span>000-000-0000</span><span>email@email.com</span>
      <span>Mark Dolan, treasurer and director</span><span>555-014-2290</span><span>mark@riversidelearnhouse.org</span>
    </div>
  </div>

  <div class="abs mission-box"></div>
  <p class="abs mission">Founded in 2004 by Lars Trulsen, the Riverside Learning House at Prek Sala is a 501(c)(3) organization dedicated to breaking the cycle of poverty of some of Cambodia's poorest children by providing a rigorous core K-9 education that emphasizes English proficiency. All donations are 100% passed through for the needs of the school. All administrative costs are paid personally by the board, and financial statements are always available on request.</p>

</div>
</body>
</html>
```